Lumo Brew Premium Matcha brand Label

This is a label design project for a luxury tea brand. Feel free to be creative within the guidelines.
Attached to this project is a document called “Private Label Design Requirements” with the design guidelines and template. There is another document called "Lumo Brew Packaging Instructions" this has more details necessary to stick to the guidelines in the first document.

I have also attached the certifications to be included as well as different variations of the logo for you to use.

If you have any questions, I am here.
Updates

Target Market(s)

Young, active, fun, enjoy the finer things

```html
<!DOCTYPE html>
<html lang="en">
<head>
<meta charset="utf-8">
<title>Lumo Brew Premium Organic Ceremonial Matcha Label</title>
<link href="https://fonts.googleapis.com/css2?family=Open+Sans:wght@400;500&display=swap" rel="stylesheet">
<style>
  :root {
    --page: #ffffff;
    --trim: #e4525a;
    --frame: #2b2b2b;
    --safe-line: #3aa9e0;
    --ink: #2e2e2e;
    --accent-rule: #2ea3dc;
    --badge: #1f7a44;
    --badge-ring: #8a4a24;
    --scene-warm: #c9b9a4;
    --scene-green: #b8c99a;
    --scene-light: #eef1f3;
  }
  html, body {
    margin: 0;
    padding: 0;
    overflow: hidden;
    background: var(--page);
  }
  .label {
    position: relative;
    width: 1200px;
    height: 234px;
    box-sizing: border-box;
    border: 1px solid var(--trim);
    background: linear-gradient(90deg, #f6f6f5 0%, #fafafa 50%, var(--scene-light) 100%);
    font-family: "Open Sans", Arial, sans-serif;
    color: var(--ink);
    overflow: hidden;
  }
  .scene {
    position: absolute;
  }
  .scene-left {
    left: 62px; top: 20px; width: 430px; height: 214px;
    background:
      radial-gradient(ellipse 38% 45% at 35% 60%, rgba(150,170,90,0.55), transparent 70%),
      radial-gradient(ellipse 40% 45% at 72% 50%, rgba(180,110,70,0.55), transparent 70%),
      radial-gradient(ellipse 30% 30% at 45% 12%, rgba(170,140,110,0.5), transparent 70%),
      linear-gradient(90deg, rgba(201,185,164,0.35) 0%, rgba(201,185,164,0.25) 70%, rgba(250,250,250,0) 100%);
    -webkit-mask-image: linear-gradient(90deg, #000 0%, #000 60%, transparent 100%);
            mask-image: linear-gradient(90deg, #000 0%, #000 60%, transparent 100%);
  }
  .scene-right {
    left: 876px; top: 0; width: 324px; height: 234px;
    background:
      radial-gradient(ellipse 30% 35% at 72% 55%, rgba(220,180,140,0.45), transparent 70%),
      radial-gradient(ellipse 25% 30% at 25% 35%, rgba(160,190,120,0.35), transparent 70%),
      linear-gradient(90deg, rgba(238,241,243,0) 0%, rgba(225,230,228,0.6) 100%);
  }
  .frame {
    position: absolute;
    left: 20px; top: 20px; width: 1160px; height: 193px;
    box-sizing: border-box;
    border: 1px solid var(--frame);
    border-radius: 20px;
  }
  .safe-area {
    position: absolute;
    left: 64px; top: 39px; width: 1072px; height: 155px;
    box-sizing: border-box;
    border: 1px dotted var(--safe-line);
    border-radius: 10px;
  }
  .line {
    position: absolute;
    margin: 0;
    line-height: 1;
    white-space: nowrap;
  }
  .distributor { left: 71px; font-size: 15.5px; }
  .brand-block { left: 443px; width: 300px; text-align: center; }
  .brand-name { font-size: 27px; letter-spacing: 0.5px; top: 124px; }
  .brand-product { font-size: 14px; top: 152px; }
  .brand-weight { font-size: 19.5px; top: 171px; }
  .ingredients-title { left: 816px; top: 42px; font-size: 13.5px; }
  .ingredients-list { left: 816px; top: 65px; font-size: 14px; }
  .accent-rule {
    position: absolute;
    left: 817px; top: 86px; width: 83px; height: 1px;
    background: var(--accent-rule);
  }
  .prep-step { left: 816px; font-size: 11.5px; }
  .cert-badge {
    position: absolute;
    left: 947px; top: 146px; width: 40px; height: 40px;
    box-sizing: border-box;
    border-radius: 50%;
    border: 2px solid var(--badge-ring);
    background: var(--badge);
  }
  .storage { left: 1000px; font-size: 13.5px; text-transform: uppercase; letter-spacing: 0.3px; }
</style>
</head>
<body>
  <div class="label">
    <div class="scene scene-left" role="img" aria-label="Photo of a clay teapot, matcha powder bowls and a bamboo whisk on a wooden table"></div>
    <div class="scene scene-right" role="img" aria-label="Faint photo of a cup of green tea with fresh tea leaves"></div>

    <div class="frame"></div>
    <div class="safe-area"></div>

    <p class="line distributor" style="top:82px">Distributed by Lumo Brew Co. | Riverton, Ga</p>
    <p class="line distributor" style="top:103px">Certified Organic by Verde Organic Board</p>
    <p class="line distributor" style="top:124px">PRODUCT OF JAPAN</p>

    <p class="line brand-block brand-name">Lumo Brew</p>
    <p class="line brand-block brand-product">Premium Organic Ceremonial Matcha</p>
    <p class="line brand-block brand-weight">Net Wt: 30g</p>

    <p class="line ingredients-title">Ingredients</p>
    <p class="line ingredients-list">Premium Organic Japanese Matcha Green Tea</p>
    <div class="accent-rule"></div>

    <p class="line prep-step" style="top:95px">• 2 tsp of Matcha</p>
    <p class="line prep-step" style="top:110px">• 2oz of Water (170-180 degrees F)</p>
    <p class="line prep-step" style="top:125px">• Whisk in a W formation until frothy</p>
    <p class="line prep-step" style="top:139px">• Sweeten to taste</p>

    <div class="cert-badge" role="img" aria-label="Organic certification badge"></div>
    <p class="line storage" style="top:150px">Keep refrigerated</p>
    <p class="line storage" style="top:168px">for quality</p>
  </div>
</body>
</html>
```